Biotech company needs graphics to describe company culture

We would like to have help in describing our company culture in a graphic way.Our "local culture" focus areas (Proud & Accountable, Challenge & Collaborate) builds on the Halvern Quist corporate values which is Integrity, Intensity, Innovation and Involvement. Our "local norms" is describing behaviours which we want to see more of, and that will ensure that we get better at our culture focus. We would like this to be expressed in a graphic way, getting an image we can use for multiple purposes in a format that fits into PowerPoint slides, can be printed on mousepads etc. We want one Norwegian and one English version. Attached is an example of the desired content in both languages.

Target Market(s)

Employees

Industry/Entity Type

Biotechnology

Font styles to use
Serif

Colors

Designer to choose colors to be used in the design.

Requirements
Nice to have
• Want the employees to intuitive understand the connection from values to cultural focus to norms. The norms are the most important to highlight to our employees. They should understand that if they do more of the desired behaviours (norms), then they will have act according to our culture focus and our values.

```html
<!DOCTYPE html>
<html lang="en">
<head>
<meta charset="utf-8">
<title>Our Culture – Halvern Quist</title>
<link rel="stylesheet" href="https://fonts.googleapis.com/css2?family=League+Gothic&family=Poppins:wght@600;700&display=swap">
<style>
  :root {
    --orange: #f95100;
    --pink: #ec1563;
    --navy: #2e3283;
    --red: #ee3a2b;
    --ink: #111111;
    --text: #2a2e3a;
    --panel: #e6e7e9;
    --footer: #262f3d;
    --white: #ffffff;
  }
  * { margin: 0; padding: 0; box-sizing: border-box; }
  html, body { width: 1200px; height: 849px; overflow: hidden; background: var(--white); }
  .poster { position: relative; width: 1200px; height: 849px; background: var(--white); font-family: "Poppins", sans-serif; }
  .structure { position: absolute; inset: 0; }

  .title {
    position: absolute; left: 0; width: 1200px; top: 44px;
    text-align: center; font-family: "League Gothic", sans-serif; font-weight: 400;
    font-size: 94px; line-height: 1; color: var(--ink); letter-spacing: 1px; word-spacing: 14px;
  }
  .band-label {
    position: absolute; top: 145px; height: 71px; line-height: 71px;
    text-align: center; color: var(--white);
    font-family: "League Gothic", sans-serif; font-weight: 400; font-size: 44px; letter-spacing: 0.3px;
  }
  .band-label.norms { left: 0; width: 470px; }
  .band-label.values { left: 478px; width: 330px; }
  .band-label.focus { left: 833px; width: 367px; }

  .norm { position: absolute; left: 107px; width: 270px; }
  .norm-panel {
    position: absolute; left: 71px; right: 0; top: 4px; bottom: 4px;
    background: var(--panel); border-radius: 10px;
  }
  .norm-panel::after {
    content: ""; position: absolute; right: -12px; top: 50%; width: 24px; height: 24px;
    margin-top: -12px; border-radius: 50%; background: var(--panel);
  }
  .norm-text {
    position: absolute; right: 19px; top: 50%; transform: translateY(-50%);
    text-align: right; color: var(--text); white-space: nowrap;
    font-weight: 700; font-size: 14px; letter-spacing: -0.3px; line-height: 20.5px; text-transform: uppercase;
  }
  .norm-tab {
    position: absolute; left: 0; top: 0; bottom: 0; width: 89px;
    border-radius: 16px 44px 44px 16px / 16px 72px 72px 16px;
    display: flex; align-items: center; justify-content: center;
  }
  .norm-tab span {
    writing-mode: vertical-rl; transform: rotate(180deg);
    color: var(--white); font-family: "League Gothic", sans-serif; font-weight: 400;
    font-size: 27px; line-height: 22px; text-align: center; text-transform: uppercase;
  }
  .norm.solution { top: 247px; height: 144px; }
  .norm.solution .norm-tab { background: var(--orange); }
  .norm.feedback { top: 440px; height: 144px; }
  .norm.feedback .norm-tab { background: var(--pink); }
  .norm.curious { top: 631px; height: 144px; }
  .norm.curious .norm-tab { background: var(--navy); }

  .value { position: absolute; left: 523px; width: 220px; height: 58px; }
  .value-bar {
    position: absolute; left: 32px; right: 0; top: 0; bottom: 0;
    background: var(--pink); border-radius: 28px 12px 0 0;
  }
  .value-icon {
    position: absolute; left: 0; top: -1px; width: 60px; height: 60px;
    border-radius: 50%; background: var(--navy); border: 3px solid var(--white);
    display: flex; align-items: center; justify-content: center;
  }
  .value-name {
    position: absolute; left: 70px; top: 0; line-height: 58px;
    color: var(--white); font-weight: 700; font-size: 18px; text-transform: uppercase;
  }
  .value.integrity { top: 361px; }
  .value.intensity { top: 445px; }
  .value.innovation { top: 527px; }
  .value.involvement { top: 615px; }

  .focus-item {
    position: absolute; left: 876px; width: 217px; height: 58px;
    background: var(--navy); border-radius: 6px 26px 0 26px;
    color: var(--white); font-weight: 700; font-size: 18px; line-height: 58px;
    text-align: center; text-transform: uppercase;
  }
  .focus-item.proud { top: 367px; }
  .focus-item.accountable { top: 451px; }
  .focus-item.challenge { top: 534px; }
  .focus-item.collaborate { top: 622px; }

  .brand {
    position: absolute; left: 799px; top: 755px; width: 309px; height: 86px;
    display: flex; align-items: center; justify-content: center;
    color: var(--red); font-weight: 700; font-size: 30px; letter-spacing: -0.5px;
  }
</style>
</head>
<body>
<main class="poster">
  <svg class="structure" width="1200" height="849" viewBox="0 0 1200 849" aria-hidden="true">
    <path class="top-tab" d="M433 0 H766 V16 Q766 32 750 32 H449 Q433 32 433 16 Z" fill="var(--red)"/>
    <polygon class="band norms" points="0,145 456,145 470,180.5 456,216 0,216" fill="var(--orange)"/>
    <polygon class="band values" points="463,145 810,145 824,180.5 810,216 463,216 477,180.5" fill="var(--pink)"/>
    <polygon class="band focus" points="818,145 1200,145 1200,216 818,216 832,180.5" fill="var(--navy)"/>

    <g class="connectors" fill="none" stroke="var(--panel)" stroke-width="7">
      <polyline points="377,319 441,319 441,702 377,702"/>
      <line x1="377" y1="510" x2="485" y2="510"/>
      <polyline points="540,390 485,390 485,644 540,644"/>
      <polyline points="730,390 769,390 769,644 730,644"/>
      <line x1="769" y1="510" x2="838" y2="510"/>
      <polyline points="890,396 838,396 838,651 890,651"/>
    </g>
    <circle cx="437" cy="510" r="12" fill="var(--red)"/>
    <circle cx="806" cy="510" r="12" fill="var(--red)"/>

    <rect class="footer" x="0" y="806" width="1200" height="43" fill="var(--footer)"/>
    <path class="brand-tab" d="M799 849 V760 H1078 Q1106 760 1106 788 V849 Z" fill="var(--white)" stroke="var(--footer)" stroke-width="5"/>
  </svg>

  <h1 class="title">OUR CULTURE</h1>
  <div class="band-label norms">OUR NORMS</div>
  <div class="band-label values">OUR VALUES</div>
  <div class="band-label focus">OUR CULTURE FOCUS</div>

  <section class="norm solution">
    <div class="norm-panel"><p class="norm-text">I take ownership,<br>am solution<br>oriented and<br>ensures<br>implementation</p></div>
    <div class="norm-tab"><span>Solution<br>oriented</span></div>
  </section>
  <section class="norm feedback">
    <div class="norm-panel"><p class="norm-text">I give and seek<br>constructive<br>feedback</p></div>
    <div class="norm-tab"><span>Constructive<br>feedback</span></div>
  </section>
  <section class="norm curious">
    <div class="norm-panel"><p class="norm-text">I am curious<br>on others<br>perspectives<br>and new ways of<br>doing things</p></div>
    <div class="norm-tab"><span>Curious</span></div>
  </section>

  <div class="value integrity">
    <div class="value-bar"></div>
    <div class="value-icon">
      <svg width="34" height="24" viewBox="0 0 34 24" fill="none" stroke="var(--white)" stroke-width="2.4" stroke-linejoin="round" stroke-linecap="round" aria-hidden="true">
        <path d="M2 6 L9 4 L17 8 L25 4 L32 6"/>
        <path d="M6 6 L6 14 L15 21 Q18 23 20 20 L27 14 L28 6"/>
        <path d="M13 10 L19 15 M16 8 L23 13"/>
      </svg>
    </div>
    <span class="value-name">Integrity</span>
  </div>
  <div class="value intensity">
    <div class="value-bar"></div>
    <div class="value-icon">
      <svg width="32" height="32" viewBox="0 0 32 32" aria-hidden="true">
        <circle cx="16" cy="16" r="7" fill="var(--white)"/>
        <g stroke="var(--white)" stroke-width="2.4" stroke-linecap="round">
          <line x1="16" y1="2" x2="16" y2="5"/><line x1="16" y1="27" x2="16" y2="30"/>
          <line x1="2" y1="16" x2="5" y2="16"/><line x1="27" y1="16" x2="30" y2="16"/>
          <line x1="6" y1="6" x2="8" y2="8"/><line x1="24" y1="24" x2="26" y2="26"/>
          <line x1="26" y1="6" x2="24" y2="8"/><line x1="8" y1="24" x2="6" y2="26"/>
        </g>
      </svg>
    </div>
    <span class="value-name">Intensity</span>
  </div>
  <div class="value innovation">
    <div class="value-bar"></div>
    <div class="value-icon">
      <svg width="32" height="32" viewBox="0 0 32 32" aria-hidden="true">
        <path d="M16 7 A8 8 0 0 1 21 21 V24 H11 V21 A8 8 0 0 1 16 7 Z" fill="var(--white)"/>
        <rect x="12" y="26" width="8" height="3" rx="1.5" fill="var(--white)"/>
        <g stroke="var(--white)" stroke-width="2" stroke-linecap="round">
          <line x1="16" y1="1" x2="16" y2="3"/><line x1="4" y1="14" x2="6" y2="14"/>
          <line x1="26" y1="14" x2="28" y2="14"/><line x1="7" y1="5" x2="8.5" y2="6.5"/>
          <line x1="25" y1="5" x2="23.5" y2="6.5"/>
        </g>
      </svg>
    </div>
    <span class="value-name">Innovation</span>
  </div>
  <div class="value involvement">
    <div class="value-bar"></div>
    <div class="value-icon">
      <svg width="32" height="30" viewBox="0 0 32 30" fill="var(--white)" aria-hidden="true">
        <circle cx="16" cy="5" r="3.5"/><path d="M10 14 Q16 6 22 14 Z"/>
        <circle cx="6" cy="18" r="3.5"/><path d="M0 27 Q6 19 12 27 Z"/>
        <circle cx="26" cy="18" r="3.5"/><path d="M20 27 Q26 19 32 27 Z"/>
      </svg>
    </div>
    <span class="value-name">Involvement</span>
  </div>

  <div class="focus-item proud">Proud</div>
  <div class="focus-item accountable">Accountable</div>
  <div class="focus-item challenge">Challenge</div>
  <div class="focus-item collaborate">Collaborate</div>

  <div class="brand">Halvern Quist</div>
</main>
</body>
</html>
```